Business card design needed

We design, manufacture and install kitchen robes vanity etc.
We have a current card that i want to upload that you can base the design around and make suggestions for other design but we need the logo to be unchanged that i will up load along with our current card.

Industry/Entity Type

Business

Contact Information for Business Card

Tallowind Joinery Works
Dorian Calvestri
47 Quarrington Avenue, Kestrel Park S.A 5092
dorian@tallowindjoinery.com.au
Lic. No. Bld 582904 Bld 740251

```html
<!DOCTYPE html>
<html lang="en">
<head>
<meta charset="utf-8">
<title>Tallowind Joinery Works – Business Card</title>
<link rel="stylesheet" href="https://fonts.googleapis.com/css2?family=Source+Sans+3:wght@400;600;700&display=swap">
<style>
  :root {
    --green: #8ea83b;
    --grey: #8b8d90;
    --paper: #ffffff;
    --paper-shade: #ecedee;
    --backdrop: #d9dadb;
    --white: #ffffff;
  }
  * { box-sizing: border-box; margin: 0; padding: 0; }
  html, body {
    width: 1200px; height: 900px; overflow: hidden;
    background: var(--backdrop);
    font-family: "Source Sans 3", sans-serif;
  }
  .canvas {
    width: 1200px; height: 900px;
    display: flex; align-items: center; justify-content: center; gap: 40px;
  }
  .card {
    position: relative;
    width: 540px; height: 330px;
    background: var(--paper);
    box-shadow: 0 6px 18px rgba(0,0,0,0.18);
    overflow: hidden;
  }

  /* Services card */
  .card--services {
    background: linear-gradient(180deg, var(--paper-shade) 0%, var(--paper) 55%);
  }
  .brand {
    display: flex; align-items: center; gap: 12px;
    color: var(--grey);
    font-weight: 700;
    text-transform: uppercase;
    letter-spacing: 0.5px;
    white-space: nowrap;
  }
  .brand__mark {
    width: 14px; height: 14px;
    background: var(--green);
    flex: none;
  }
  .card--services .brand {
    position: absolute; top: 84px; left: 0; right: 0;
    justify-content: center;
    font-size: 30px;
  }
  .services-band {
    position: absolute; left: 0; right: 0; bottom: 34px; height: 124px;
    background: var(--green);
    color: var(--white);
    text-align: center;
    padding-top: 16px;
  }
  .services-band__label {
    font-size: 17px; font-weight: 400; letter-spacing: 0.6px;
    text-transform: uppercase;
  }
  .services-band__line {
    font-size: 21px; font-weight: 700; line-height: 1.25;
  }

  /* Contact card */
  .card--contact .brand {
    position: absolute; top: 44px; left: 130px;
    font-size: 22px;
  }
  .person {
    position: absolute; top: 92px; left: 150px;
    color: var(--green);
    font-size: 21px; font-weight: 400;
  }
  .licence {
    position: absolute; top: 142px; right: 22px;
    color: var(--grey);
    font-size: 9.5px;
  }
  .contact-band {
    position: absolute; left: 0; right: 0; top: 160px; height: 126px;
    background: var(--green);
    color: var(--white);
    display: flex; justify-content: space-between;
    padding: 14px 24px 0 26px;
  }
  .contact-band__company { font-size: 16px; font-weight: 700; line-height: 1.25; }
  .contact-band__line { font-size: 15px; font-weight: 400; line-height: 1.25; }
  .phones {
    align-self: flex-end;
    padding-bottom: 14px;
    display: grid; grid-template-columns: auto auto; column-gap: 8px;
    font-size: 17px; line-height: 1.15;
  }
  .phones__key { font-weight: 700; text-align: right; }
</style>
</head>
<body>
<main class="canvas">

  <section class="card card--services" aria-label="Business card, services side">
    <div class="brand"><span class="brand__mark"></span><span>Tallowind Joinery Works</span></div>
    <div class="services-band">
      <p class="services-band__label">Custom made</p>
      <p class="services-band__line">Kitchens • Vanities • Laundry</p>
      <p class="services-band__line">Robes • Entertainment units • Flat packs</p>
    </div>
  </section>

  <section class="card card--contact" aria-label="Business card, contact side">
    <div class="brand"><span class="brand__mark"></span><span>Tallowind Joinery Works</span></div>
    <p class="person">Dorian Calvestri</p>
    <p class="licence">Lic. No.: Bld 582904, Bld 740251</p>
    <div class="contact-band">
      <div class="contact-band__details">
        <p class="contact-band__company">Tallowind Joinery Works</p>
        <p class="contact-band__line">47 Quarrington Avenue, Kestrel Park S.A 5092</p>
        <p class="contact-band__line">dorian@tallowindjoinery.com.au</p>
      </div>
      <div class="phones">
        <span class="phones__key">P</span><span>(08) 7010 4826</span>
        <span class="phones__key">f</span><span>(08) 7010 4839</span>
        <span class="phones__key">m</span><span>0491 570 318</span>
      </div>
    </div>
  </section>

</main>
</body>
</html>
```